Marlow Poise & Image Consultancy

Hi, I need a brochure design for my personal styling business. I have downloaded the company logo along with the content of the services offered for the brochure. Being a colour and styling business I would been keen on having some pictures of timeless fashion or colour samples, This is not absolutely necessary just an idea. I had also thought about changing and naming the services offered with a feminine, fun interesting type of theme. This may make it more inviting, I would be really interested in any of your creative ideas in this area. I will be deciding on the business card design in the next couple of days. I will download the design for this once I have made the decision. I will be okay to pay for any photo images that may be required if the brochure is selected. I had envisaged a tri fold brochure standard letter size with two folds (8.5" by 11inchs) however I am open to any suggestions. Please feel free to make any changes or modification's to the content, font etc in the files downloaded for the brochure. Many Thanks.
Updates
Project Deadline Extended
Reason: I need to extend the time for this project as I do not have all of content required for the brochure confirmed. Many Thanks
Industry/Entity Type
Fashion
Font styles to use
Look and feel
Each slider illustrates characteristics of the customer's brand and the style your logo design should communicate.

```html
<!DOCTYPE html>
<html lang="en">
<head>
<meta charset="utf-8">
<title>Marlow Poise &amp; Image Consultancy – Brochure</title>
<link rel="stylesheet" href="https://fonts.googleapis.com/css2?family=Didact+Gothic&display=swap">
<style>
  :root {
    --backdrop-top: #34404c;
    --backdrop-bottom: #121a23;
    --sheet: #1a1714;
    --sheet-deep: #0f0d0b;
    --gold: #e9c968;
    --gold-soft: #f4df98;
    --copy: #d8d0c0;
    --font: "Didact Gothic", "Century Gothic", sans-serif;
  }
  * { box-sizing: border-box; margin: 0; padding: 0; }
  html, body { width: 1200px; height: 900px; overflow: hidden; }
  body {
    position: relative;
    background: radial-gradient(ellipse at 40% 20%, var(--backdrop-top), var(--backdrop-bottom) 75%);
    font-family: var(--font);
    color: var(--copy);
  }

  /* ---------- sheets ---------- */
  .sheet {
    position: absolute;
    display: flex;
    background: var(--sheet);
    overflow: hidden;
    box-shadow: 0 8px 24px rgba(0,0,0,.45);
  }
  .sheet::before, .sheet::after {
    content: "";
    position: absolute;
    left: 0; right: 0;
    height: 4px;
    background: var(--gold);
    z-index: 2;
  }
  .sheet::before { top: 10px; }
  .sheet::after { bottom: 10px; }

  .cover         { left: 20px;  top: 20px;  width: 360px;  height: 270px; }
  .spread-party  { left: 400px; top: 20px;  width: 780px;  height: 270px; }
  .spread-dress  { left: 20px;  top: 310px; width: 570px;  height: 270px; }
  .spread-colour { left: 610px; top: 310px; width: 570px;  height: 270px; }
  .spread-style  { left: 20px;  top: 600px; width: 1160px; height: 280px; }

  /* ---------- photo placeholders ---------- */
  .photo { flex: none; height: 100%; }
  .photo-stack { flex: none; display: flex; flex-direction: column; height: 100%; }
  .photo-stack .photo { height: 50%; }
  .tone-violet  { background: linear-gradient(160deg, #5b4a6e, #c9a3b8 55%, #2a2230); }
  .tone-pink    { background: linear-gradient(150deg, #2b2a33, #e7b8c4 60%, #f2d6d2); }
  .tone-blonde  { background: linear-gradient(160deg, #d9bd86, #f0d8c4 55%, #9c7a58); }
  .tone-brick   { background: linear-gradient(170deg, #8d4a3a, #b9a890 55%, #3b3634); }
  .tone-denim   { background: linear-gradient(170deg, #e9e6e2, #5d83a8 45%, #c8ab92); }
  .tone-palette { background: linear-gradient(140deg, #8fb5e8, #b28fe0 40%, #6fd46b 70%, #2d2a2f); }
  .tone-meadow  { background: linear-gradient(170deg, #8fa37a, #efe3cf 50%, #b7c79c); }
  .tone-crowd   { background: linear-gradient(160deg, #7f8a6f, #c99b77 55%, #5e4a3e); }
  .tone-shop    { background: linear-gradient(170deg, #d5d2cf, #d87aa6 55%, #6b9fb8); }
  .tone-bride   { background: linear-gradient(170deg, #3d4a2f, #ece8da 55%, #6b6a52); }

  .photo-narrow { width: 110px; }
  .photo-mid    { width: 160px; }
  .photo-wide   { width: 210px; }

  /* ---------- copy columns ---------- */
  .column {
    flex: 1;
    min-width: 0;
    padding: 24px 10px 22px;
    font-size: 8px;
    line-height: 1.4;
  }
  .column h2 {
    font-weight: 400;
    font-size: 11px;
    color: var(--gold-soft);
    text-align: center;
    white-space: nowrap;
    margin-bottom: 6px;
  }
  .column h3 {
    font-weight: 400;
    font-size: 10px;
    color: var(--gold-soft);
    white-space: nowrap;
    margin: 8px 0 4px;
  }
  .column p { margin-bottom: 5px; }
  .column .price { color: var(--gold); }
  .column ul { list-style: none; margin-bottom: 5px; }
  .column li::before { content: "• "; color: var(--gold); }

  /* ---------- cover ---------- */
  .cover { flex-direction: column; background: var(--sheet-deep); }
  .cover-top { display: flex; height: 190px; }
  .cover-top .photo { width: 190px; }
  .cover-dark { flex: 1; background: linear-gradient(180deg, #1c1a18, #0e0c0b); }
  .cover::before { top: 190px; }
  .cover-brand {
    flex: 1;
    display: flex;
    align-items: center;
    justify-content: flex-end;
    gap: 8px;
    padding: 0 18px 12px;
  }
  .brand-dot {
    width: 16px; height: 16px;
    border-radius: 50%;
    background: var(--gold);
    flex: none;
  }
  .brand-name {
    font-size: 14px;
    font-weight: 400;
    color: var(--gold);
    white-space: nowrap;
  }
</style>
</head>
<body>

  <!-- Cover -->
  <section class="sheet cover">
    <div class="cover-top">
      <div class="photo tone-violet" role="img" aria-label="Portrait of a model with violet eye make-up and lips"></div>
      <div class="cover-dark"></div>
    </div>
    <div class="cover-brand">
      <span class="brand-dot"></span>
      <span class="brand-name">Marlow Poise &amp; Image Consultancy</span>
    </div>
  </section>

  <!-- Party spread -->
  <section class="sheet spread-party">
    <div class="photo-stack photo-mid">
      <div class="photo tone-pink" role="img" aria-label="Model with dark hair and bright pink lipstick"></div>
      <div class="photo tone-blonde" role="img" aria-label="Smiling blonde model with natural make-up"></div>
    </div>
    <div class="column">
      <h3>Swatch &amp; Sparkle Gathering</h3>
      <p>Gather your friends for an evening of colour. Each guest discovers the shades that flatter her skin, eyes and hair, and leaves with a personal swatch wallet.</p>
      <p class="price">Price: $45 per person, minimum four guests.</p>
      <h3>Brush &amp; Blush Evening</h3>
      <p>A relaxed session where every guest learns a quick day look and an evening look using her own make up bag.</p>
      <p class="price">Price: $40 per person.</p>
    </div>
    <div class="column">
      <p>Discover how to dress without the stress. Includes a wardrobe review and a personal shopping list.</p>
      <p class="price">Price $300.00</p>
      <h3>Grand Soirée Evening</h3>
      <p>Get a group of friends together and enjoy a full day of colour, style and make up advice, finished with drinks and a mini photo shoot.</p>
      <h3>Silhouette Social</h3>
      <p>Learn which shapes, cuts and fabrics suit your body and how to build outfits that work for every occasion.</p>
      <p class="price">Price: $50 per person, 3 hours.</p>
    </div>
    <div class="photo tone-brick photo-mid" role="img" aria-label="Two models in tall hats and patterned skirts against a brick wall"></div>
  </section>

  <!-- Dress & make up spread -->
  <section class="sheet spread-dress">
    <div class="photo tone-denim photo-narrow" role="img" aria-label="Model in a denim shirt and beige skirt"></div>
    <div class="column">
      <h2>Dress for the life you love</h2>
      <p>Time for a change? Take a fresh look at your wardrobe and discover how to dress in a way that reflects your personality and lifestyle.</p>
      <ul>
        <li>Personal colour analysis</li>
        <li>Body shape styling</li>
        <li>Wardrobe review</li>
        <li>Personal shopping</li>
        <li>Make up lessons</li>
      </ul>
    </div>
    <div class="column">
      <h2>Marlow Make Up Services</h2>
      <p>Get ready for a special event or simply refresh your everyday look. Our artists use quality products to enhance your natural features.</p>
      <p class="price">Make up lesson, 90 minutes: $90</p>
      <p class="price">Bridal trial and wedding day: $250</p>
    </div>
    <div class="photo tone-palette photo-narrow" role="img" aria-label="Eyeshadow palette with brushes"></div>
  </section>

  <!-- Colour spread -->
  <section class="sheet spread-colour">
    <div class="photo tone-meadow photo-narrow" role="img" aria-label="Laughing young woman in a cream blouse outdoors"></div>
    <div class="column">
      <p>Discover the colours and styles that make you glow, with a gift voucher ready to give.</p>
      <h3>The Always Radiant Package</h3>
      <ul>
        <li>Colour consultation</li>
        <li>Style consultation</li>
        <li>Make up lesson</li>
      </ul>
      <p class="price">Price $395.00</p>
      <h3>The Grand Closet Refresh</h3>
      <p>A complete review of your wardrobe with a guided shopping trip.</p>
    </div>
    <div class="column">
      <h2>Marlow colour consultation</h2>
      <p>Colour has a huge impact on the way we look and feel. Wearing the right shades brightens the skin and brings out the eyes.</p>
      <ul>
        <li>Your personal colour palette</li>
        <li>Best neutrals and accents</li>
        <li>Make up colours to match</li>
      </ul>
      <p class="price">Price: $180, 2 hours</p>
    </div>
    <div class="photo tone-crowd photo-narrow" role="img" aria-label="Smiling woman in a city street"></div>
  </section>

  <!-- Style spread -->
  <section class="sheet spread-style">
    <div class="photo tone-shop photo-wide" role="img" aria-label="Young woman in a striped top holding shopping bags"></div>
    <div class="column">
      <h3>Marlow Seasonal Update</h3>
      <p>Keep up with the changing seasons. We review trends, colours and key pieces and show you how to add them to the clothes you already own.</p>
      <p class="price">Price: $120</p>
      <h3>Final Flourish Session</h3>
      <p>Accessories, shoes and bags chosen to complete your look.</p>
      <p class="price">Price: $85</p>
      <h3>Closet Edit</h3>
      <p>We sort what to keep, alter or let go, then plan the pieces that will fill the gaps.</p>
      <p class="price">Price: $250, 3 hours</p>
    </div>
    <div class="column">
      <h2>Marlow Style Consultation</h2>
      <p>Do you find yourself staring into a full wardrobe with nothing to wear? Learn which shapes and proportions flatter your figure and personality.</p>
      <ul>
        <li>Your body shape explained</li>
        <li>Best cuts, necklines and lengths</li>
        <li>A style guide to keep</li>
      </ul>
      <p class="price">Price: $180, 2 hours</p>
    </div>
    <div class="photo tone-bride photo-wide" role="img" aria-label="Woman in an ivory evening gown in a garden"></div>
  </section>

</body>
</html>
```